Halvercott Orthodontics business card

Using our existing logo (created with ArtFolio), please create a tasteful, contemporary business card. We are father and daughter orthodontists specializing in braces, clarafit, etc to design healthy, beautiful smiles for children, adolescents, and adults. We would like the design to be family-friendly but not childish.
The final design should include all of the information without looking cluttered (I hope! If necessary to achieve an optimal design, please consider making the card double-sided)
Purple, black, silver on a white card
Please include the following information:
Halvercott Orthodontics (logo)
Marguerite L. Halvercott, DMD
Douglas R. Halvercott, DMD

312 Bramblewood Street
North Andover, MA 01899
978.555.0142

847C Quarry Hollow Street
Methuen, MA 01898
978.555.0187

email frontdesk@halvercottortho.example
website www.halvercottortho.example

```html
<!DOCTYPE html>
<html lang="en">
<head>
<meta charset="utf-8">
<title>Halvercott Orthodontics — Business Card</title>
<link href="https://fonts.googleapis.com/css2?family=Montserrat:wght@400;500;700&display=swap" rel="stylesheet">
<style>
  :root {
    --backdrop: #9a9a9a;
    --card-white: #ffffff;
    --brand-purple: #662d91;
    --deep-purple: #4f2a7d;
    --soft-purple: #7a55a3;
    --ink: #1e1e1e;
    --silver: #dcdce2;
  }
  * { margin: 0; padding: 0; box-sizing: border-box; }
  html, body {
    width: 1093px; height: 1200px; overflow: hidden;
    background: var(--backdrop);
    font-family: "Montserrat", sans-serif;
  }
  .card {
    position: absolute;
    left: 264px;
    width: 581px;
    height: 364px;
    border-radius: 17px;
    overflow: hidden;
  }
  .card-front { top: 225px; background: var(--card-white); }
  .card-back { top: 616px; }

  .brand {
    position: absolute;
    left: 34px; top: 184px;
    display: flex; align-items: center; gap: 9px;
  }
  .brand-dot {
    width: 34px; height: 34px; border-radius: 50%;
    background: var(--brand-purple);
    flex: none;
  }
  .brand-name {
    color: var(--brand-purple);
    font-weight: 700;
    font-size: 17px;
    line-height: 1.2;
    letter-spacing: 0.3px;
  }

  .divider {
    position: absolute;
    left: 263px; top: 115px;
    width: 1.5px; height: 162px;
    background: var(--brand-purple);
  }
  .details { position: absolute; left: 276px; top: 113px; color: var(--ink); }
  .person-name {
    color: var(--brand-purple);
    font-weight: 700;
    font-size: 16px;
    line-height: 20px;
    white-space: nowrap;
  }
  .person-title { font-size: 13px; line-height: 17px; }
  .address { margin-top: 14px; font-size: 13px; line-height: 17px; }
  .contact-list { list-style: none; margin-top: 16px; }
  .contact-item {
    display: flex; align-items: center; gap: 8px;
    font-size: 13px; line-height: 22px; white-space: nowrap;
  }
  .contact-icon { width: 13px; height: 13px; flex: none; fill: var(--brand-purple); }

  .accent-band {
    position: absolute; left: 0; right: 0; bottom: 0;
    height: 15px; background: var(--brand-purple);
  }

  .back-pattern {
    position: absolute; inset: 0;
    background:
      radial-gradient(ellipse at 0% 0%, var(--soft-purple) 0%, rgba(122,85,163,0) 55%),
      var(--deep-purple);
  }
  .back-details {
    position: absolute;
    left: 34px; top: 236px;
    color: var(--silver);
  }
  .back-details .person-name { color: var(--silver); }
  .back-details .address { margin-top: 8px; }
  .back-details .contact-item { margin-top: 6px; }
  .back-details .contact-icon { fill: var(--silver); }
  .back-name {
    position: absolute;
    right: 24px; bottom: 66px;
    color: var(--silver);
    font-weight: 500;
    font-size: 10px;
    letter-spacing: 0.5px;
  }
</style>
</head>
<body>

<section class="card card-front">
  <div class="brand">
    <span class="brand-dot"></span>
    <span class="brand-name">Halvercott<br>Orthodontics</span>
  </div>

  <div class="divider"></div>

  <div class="details">
    <h1 class="person-name">Marguerite L. Halvercott, DMD</h1>
    <p class="person-title">Managing Director</p>
    <p class="address">312 Bramblewood Street<br>North Andover, MA 01899</p>
    <ul class="contact-list">
      <li class="contact-item">
        <svg class="contact-icon" viewBox="0 0 24 24"><path d="M6.6 10.8a15.1 15.1 0 0 0 6.6 6.6l2.2-2.2a1 1 0 0 1 1-.25 11.4 11.4 0 0 0 3.6.57 1 1 0 0 1 1 1V20a1 1 0 0 1-1 1A17 17 0 0 1 3 4a1 1 0 0 1 1-1h3.5a1 1 0 0 1 1 1c0 1.25.2 2.45.57 3.6a1 1 0 0 1-.25 1z"/></svg>
        978.555.0142
      </li>
      <li class="contact-item">
        <svg class="contact-icon" viewBox="0 0 24 24"><path d="M2 5h20v2l-10 6L2 7z M2 9l10 6 10-6v10H2z"/></svg>
        frontdesk@halvercottortho.example
      </li>
      <li class="contact-item">
        <svg class="contact-icon" viewBox="0 0 24 24"><circle cx="12" cy="12" r="10"/><path d="M7 8c2 0 3 1 3 3s-2 2-2 4 1 3 1 5M15 4c0 2 2 3 4 3M14 13c1 0 3 1 3 3s-1 3-1 4" stroke="#fff" stroke-width="1.6" fill="none"/></svg>
        www.halvercottortho.example
      </li>
    </ul>
  </div>

  <div class="accent-band"></div>
</section>

<section class="card card-back">
  <div class="back-pattern" role="img" aria-label="Repeating faint brand-symbol pattern on a deep purple background, fading from light at top left"></div>
  <div class="back-details">
    <h2 class="person-name">Douglas R. Halvercott, DMD</h2>
    <p class="address">847C Quarry Hollow Street<br>Methuen, MA 01898</p>
    <p class="contact-item">
      <svg class="contact-icon" viewBox="0 0 24 24"><path d="M6.6 10.8a15.1 15.1 0 0 0 6.6 6.6l2.2-2.2a1 1 0 0 1 1-.25 11.4 11.4 0 0 0 3.6.57 1 1 0 0 1 1 1V20a1 1 0 0 1-1 1A17 17 0 0 1 3 4a1 1 0 0 1 1-1h3.5a1 1 0 0 1 1 1c0 1.25.2 2.45.57 3.6a1 1 0 0 1-.25 1z"/></svg>
      978.555.0187
    </p>
  </div>
  <span class="back-name">Halvercott Orthodontics</span>
</section>

</body>
</html>
```